Holbys Pet Care

Hi. I need a business card /logo for my pet care business. Im thinking about a dogs paw print. Although i do look after other pets so don't want to restrict my self. Open to suggestions on colour etc but like greens and purples.The name of my business is holby's pet care. The logo could be just an image or have holbys power care on it. An option to do either would be great. For the winner i also would like a Web page (word press template if possible) designed if you can, of course I'll pay additional for this. Look forward to your ideas!

```html
<!DOCTYPE html>
<html lang="en">
<head>
<meta charset="utf-8">
<title>Holby's Pet Care – Business Card</title>
<link href="https://fonts.googleapis.com/css2?family=Kurale&display=swap" rel="stylesheet">
<style>
  :root{
    --backdrop:#2a2a2c;
    --card-light:#ebe3f1;
    --purple-deep:#552a8a;
    --purple-mid:#7b2f9c;
    --magenta:#a8479f;
    --pink:#c468b0;
    --brand-purple:#6a2d91;
    --ink:#151018;
  }
  *{box-sizing:border-box;margin:0;padding:0}
  html,body{width:1200px;height:800px;overflow:hidden}
  body{background:var(--backdrop);font-family:"Kurale",Georgia,serif;position:relative}
  .card{position:absolute;width:525px;height:300px;border-radius:18px;overflow:hidden;background:var(--card-light);box-shadow:0 10px 30px rgba(0,0,0,.45)}
  .card--front{left:45px;top:250px}
  .card--back{left:630px;top:250px}
  .card__art{position:absolute;inset:0;width:100%;height:100%}
  .brand-name{position:absolute;color:var(--brand-purple);font-weight:400;white-space:nowrap;line-height:1}
  .card--front .brand-name{left:30px;top:34px;font-size:42px}
  .card--back .brand-name{right:26px;top:66px;font-size:30px}
  .contact{position:absolute;right:26px;bottom:22px;text-align:right;color:var(--ink);font-size:21px;line-height:1.22;letter-spacing:.5px}
  .contact__name{font-size:22px}
  .contact__role{font-size:20px;opacity:.85}
  .back-phone{position:absolute;left:30px;top:118px;color:var(--ink);font-size:25px;letter-spacing:2px}
</style>
</head>
<body>

<section class="card card--front" aria-label="Business card front">
  <svg class="card__art" viewBox="0 0 525 300" preserveAspectRatio="none">
    <defs>
      <linearGradient id="frontBand" x1="0" y1="1" x2="1" y2="0">
        <stop offset="0" stop-color="var(--pink)"/>
        <stop offset=".45" stop-color="var(--magenta)"/>
        <stop offset="1" stop-color="var(--purple-deep)"/>
      </linearGradient>
    </defs>
    <path d="M0,132 C140,150 260,80 525,38 L525,300 L0,300 Z" fill="url(#frontBand)"/>
    <path d="M170,300 C300,240 400,140 525,100 L525,300 Z" fill="var(--purple-deep)" opacity=".7"/>
    <path d="M0,250 C170,200 330,150 525,105" stroke="#fff" stroke-opacity=".35" stroke-width="10" fill="none"/>
    <path d="M0,265 C180,215 340,165 525,125" stroke="#fff" stroke-opacity=".18" stroke-width="6" fill="none"/>
    <g role="img" aria-label="Trail of paw prints crossing the card">
      <ellipse cx="250" cy="180" rx="230" ry="28" transform="rotate(-14 250 180)" fill="var(--purple-deep)" opacity=".35"/>
    </g>
  </svg>
  <div class="brand-name">Holby's pet care</div>
  <div class="contact">
    <div class="contact__name">Mara</div>
    <div>012-345-6789</div>
    <div>hello@holbyspetcare.co.uk</div>
    <div class="contact__role">F6 name</div>
  </div>
</section>

<section class="card card--back" aria-label="Business card back">
  <svg class="card__art" viewBox="0 0 525 300" preserveAspectRatio="none">
    <defs>
      <linearGradient id="backBand" x1="0" y1="0" x2="1" y2="1">
        <stop offset="0" stop-color="var(--purple-deep)"/>
        <stop offset=".55" stop-color="var(--magenta)"/>
        <stop offset="1" stop-color="var(--pink)"/>
      </linearGradient>
    </defs>
    <path d="M0,0 L200,0 C290,20 300,170 400,230 C450,262 490,268 525,270 L525,300 L0,300 Z" fill="url(#backBand)"/>
    <path d="M0,0 L150,0 C230,40 240,200 320,300 L0,300 Z" fill="var(--purple-deep)" opacity=".55"/>
    <path d="M120,0 C220,60 260,200 420,300" stroke="#fff" stroke-opacity=".3" stroke-width="9" fill="none"/>
    <g role="img" aria-label="Trail of paw prints running down the card">
      <ellipse cx="260" cy="150" rx="170" ry="30" transform="rotate(55 260 150)" fill="var(--purple-deep)" opacity=".35"/>
    </g>
  </svg>
  <div class="back-phone">012-345-6789</div>
  <div class="brand-name">Holby's pet care</div>
</section>

</body>
</html>
```